professional looking data specialist website

I've recently had a new logo designed and I'm now looking to get a professional looking website built. This is for a new company that specialises in data. We look to support companies with business intelligence, report modelling, data governance to new european legislation (GDPR). We are offer consultancy or we can attend site and complete work when required. Our target arket is united kingdom wide and we are specifically aiming at small to medium sized companies.

Target Market(s)

small to medium enterprise companies from all industries

Industry/Entity Type

Professional Service

Coding

Coded - Design and coding required

Number of Pages Required

4 page

Font styles to use
Sans Serif

Colors

Designer to choose colors to be used in the design.

Requirements
Must have
• Professional look including the company logo, need to have ability to request more information from us so needs a inquiries page, seperate pages for the different offerings, data governance, report modelling, business intelligence implementation, data protection
Nice to have
• any website interaction, animation, etc
Should not have
• too many colours, too busy pages, must look professional

```html
<!DOCTYPE html>
<html lang="en">
<head>
<meta charset="utf-8">
<title>Harlow Data Ltd</title>
<link href="https://fonts.googleapis.com/css2?family=Open+Sans:wght@400;600;700&display=swap" rel="stylesheet">
<style>
:root{
  --blue:#2f8fd8;
  --blue-dark:#1f6fb3;
  --navy:#2b3a55;
  --text:#444b55;
  --muted:#8a9099;
  --line:#d5d8dc;
  --band:#eceeef;
  --white:#ffffff;
}
*{margin:0;padding:0;box-sizing:border-box}
html,body{width:882px;height:1200px;overflow:hidden;background:var(--white);font-family:"Open Sans",Arial,sans-serif;color:var(--text)}
.page{position:relative;width:882px;height:1200px}

/* header */
.site-header{position:relative;height:103px;background:var(--white)}
.brand{position:absolute;left:30px;top:20px;display:flex;align-items:center;gap:8px}
.brand-mark{width:26px;height:26px;background:var(--blue)}
.brand-name{font-size:28px;font-weight:600;color:var(--navy);letter-spacing:-.3px}
.info-bar{position:absolute;right:22px;top:0;height:24px;width:330px;background:var(--blue);clip-path:polygon(0 0,100% 0,100% 100%,6% 100%);display:flex;align-items:center;justify-content:center;gap:6px;color:var(--white);font-size:8px;font-weight:600;letter-spacing:.4px;padding-left:20px}
.info-bar svg{width:9px;height:9px}
.main-nav{position:absolute;right:30px;top:72px;display:flex;align-items:center;gap:16px}
.main-nav a{font-size:10px;font-weight:700;color:var(--navy);text-decoration:none;letter-spacing:.3px}
.main-nav a.active{border-bottom:2px solid var(--blue);padding-bottom:2px}
.main-nav .cta{background:var(--blue);color:var(--white);padding:6px 12px;border-radius:2px}

/* hero */
.hero{height:442px;background:linear-gradient(100deg,#e9eef3 0%,#d8e2ec 35%,#b9cde2 60%,#f1f4f7 100%)}

/* welcome */
.welcome{padding:26px 78px 0;text-align:center}
.section-title{display:flex;align-items:center;justify-content:center;gap:18px;font-size:17px;font-weight:700;color:var(--navy)}
.section-title::before,.section-title::after{content:"";width:140px;height:1px;background:var(--line)}
.welcome p{margin-top:18px;font-size:9.5px;line-height:1.65;color:var(--muted);text-align:justify}

/* contact */
.contact{position:absolute;left:0;top:715px;width:882px;height:330px;background:var(--band);text-align:center;padding-top:44px}
.contact .section-title::before,.contact .section-title::after{background:#c9ccd0;width:80px}
.contact-form{width:712px;margin:18px auto 0}
.form-row{display:flex;gap:18px}
.field{flex:1;height:30px;background:var(--white);border:1px solid #cfd3d7;font-size:10px;color:var(--text);text-align:left;padding:9px 10px}
.field.message{display:block;height:92px;margin-top:14px}
.submit{display:inline-block;margin-top:16px;background:var(--navy);color:var(--white);font-size:9px;font-weight:700;letter-spacing:.4px;padding:8px 16px;border-radius:3px}

/* footer */
.site-footer{position:absolute;left:0;top:1045px;width:882px;height:155px;text-align:center}
.footer-notch{position:absolute;left:341px;top:-14px;width:200px;height:30px;background:var(--white);border-radius:50% 50% 0 0/100% 100% 0 0}
.footer-brand{position:relative;display:flex;flex-direction:column;align-items:center;gap:8px;padding-top:20px}
.footer-brand .brand-mark{width:30px;height:30px}
.footer-brand .brand-name{font-size:26px}
.copyright{position:absolute;left:0;right:0;top:125px;font-size:7px;color:var(--muted);letter-spacing:.4px}
</style>
</head>
<body>
<div class="page">
  <header class="site-header">
    <div class="brand"><span class="brand-mark"></span><span class="brand-name">Harlow Data Ltd</span></div>
    <div class="info-bar">
      <svg viewBox="0 0 10 10"><path d="M2 1l2 2-1 1.2a6 6 0 002.8 2.8L7 6l2 2-1.3 1.3C4.5 9.3.7 5.5.7 2.3z" fill="#fff"/></svg>
      FOR INFORMATION – 0800 555 0142
    </div>
    <nav class="main-nav">
      <a class="active" href="#">HOME</a>
      <a href="#">ABOUT</a>
      <a href="#">SERVICES</a>
      <a href="#">CONTACT</a>
      <a class="cta" href="#">GET STARTED</a>
    </nav>
  </header>

  <section class="hero" role="img" aria-label="Photo of three colleagues in an office reviewing reports together at a desk"></section>

  <section class="welcome">
    <h1 class="section-title">Welcome to Harlow Data Ltd</h1>
    <p>We help small and medium sized companies across the United Kingdom turn their data into clear decisions. Our consultants design business intelligence platforms, build report models that people trust and guide your teams through data governance and the new European data protection rules. Work with us remotely as advisers, or invite us on site to deliver the project from start to finish. Every engagement begins with a short conversation about your goals, your systems and the questions your business needs to answer, and ends with tools your people can run with confidence.</p>
  </section>

  <section class="contact">
    <h2 class="section-title">Contact Us</h2>
    <div class="contact-form">
      <div class="form-row">
        <div class="field">Your Name</div>
        <div class="field">Your Email</div>
        <div class="field">Your Subject</div>
      </div>
      <div class="field message">Message</div>
      <span class="submit">SEND YOUR MESSAGE</span>
    </div>
  </section>

  <footer class="site-footer">
    <div class="footer-notch"></div>
    <div class="footer-brand"><span class="brand-mark"></span><span class="brand-name">Harlow Data Ltd</span></div>
    <p class="copyright">© 2017 HARLOW DATA LTD. ALL RIGHTS RESERVED</p>
  </footer>
</div>
</body>
</html>
```